Rostane - telephone directory add

We need simple artwork advertisement for insertion in a local yellow pages telephone directory
Design brief for telephone ads
This project is to provide a pair of 62mm high x 91mm wide ‘yellow page adds’ for our company to place in a local phone book.
• They should reflect the same theme
• They should be based on a white ‘knock out’ background (printed on yellow paper) and have one colour in addition to black.
• Rostane is our trading name
• Main contact details are www.Rostane.example, telephone 417652, sales@rostane, social.example/rostanemotortrading
• Our address is Petites Vergees Lane, Les Corvets, GY9 7QX
• First box
o Vehicle sales – (we would like to promote)
 Japanese Minivan specialist
 European & UK vehicles supplied at best prices
 Vans and light commercials available
 Trusted supplier with 20 years experience

• Second box
o Service and repairs to all models
 Popular £99 service health check
 Qualified mechanics
 Wheel alignment & Air conditioning
 Fleet servicing options

Target Market(s)

local readers

Industry/Entity Type

Automotive

Requirements
Must have
• Design brief for telephone ads
• This project is to provide a pair of 62mm high x 91mm wide ‘yellow page adds’ for our company to place in a local phone book.
• • They should reflect the same theme
• • They should be based on a white ‘knock out’ background (printed on yellow paper) and have one colour in addition to black.
• • Rostane is our trading name
• • Main contact details are www.Rostane.example, telephone 417652, sales@rostane, social.example/rostanemotortrading
• • Our address is Petites Vergees Lane, Les Corvets, GY9 7QX
• • First box
• o Vehicle sales – (we would like to promote)
•  Japanese Minivan specialist
•  European & UK vehicles supplied at best prices
•  Vans and light commercials available
•  Trusted supplier with 20 years experience
• • Second box
• o Service and repairs to all models
•  Popular £99 service health check
•  Qualified mechanics
•  Wheel alignment & Air conditioning
•  Fleet servicing options
Nice to have
• see attached word doc
• • First box
• • Second box
•  Qualified mechanics

```html
<!DOCTYPE html>
<html lang="en">
<head>
<meta charset="utf-8">
<title>Rostane – directory adverts</title>
<link rel="stylesheet" href="https://fonts.googleapis.com/css2?family=Michroma&family=Open+Sans:wght@600;700;800&family=Encode+Sans+Condensed:wght@400&display=swap">
<style>
  :root {
    --page: #e4e4e4;
    --paper: #ffffff;
    --ink: #0b0b0b;
    --panel: #262626;
    --accent: #3657d4;
    --light: #f4f4f4;
  }
  html, body {
    margin: 0;
    width: 960px;
    height: 1200px;
    overflow: hidden;
    background: var(--page);
  }
  .advert {
    position: absolute;
    left: 186px;
    width: 590px;
    height: 402px;
    display: block;
  }
  .advert--sales { top: 150px; }
  .advert--service { top: 670px; }
  .paper { fill: var(--paper); }
  .band { fill: var(--ink); }
  .panel { fill: var(--panel); }
  .brand-name {
    font-family: "Open Sans", sans-serif;
    font-weight: 800;
    font-size: 50px;
    fill: var(--accent);
  }
  .brand-dot { fill: var(--accent); }
  .contact {
    font-family: "Encode Sans Condensed", sans-serif;
    font-size: 17px;
    fill: var(--light);
  }
  .box-title {
    font-family: "Michroma", sans-serif;
    font-size: 21px;
    fill: var(--light);
    stroke: var(--light);
    stroke-width: 0.7;
  }
  .feature {
    font-family: "Open Sans", sans-serif;
    font-weight: 600;
    font-size: 19px;
    fill: var(--ink);
  }
  .strong { font-weight: 800; }
  .bar-text {
    font-family: "Encode Sans Condensed", sans-serif;
    font-size: 19px;
    fill: var(--light);
  }
  .icon-line { fill: none; stroke: currentColor; stroke-width: 1.6; stroke-linecap: round; stroke-linejoin: round; }
  .icon-fill { fill: currentColor; }
  .on-dark { color: var(--light); }
  .on-light { color: var(--ink); }
</style>
</head>
<body>

<svg width="0" height="0" style="position:absolute" aria-hidden="true">
  <defs>
    <symbol id="icon-tick" viewBox="-8 -8 16 16">
      <circle class="icon-line" r="6.5" />
      <path class="icon-line" d="M-3 0 L-0.5 2.8 L6 -4.5" />
    </symbol>
    <symbol id="icon-web" viewBox="-7 -7 14 14">
      <circle class="icon-fill" r="5.5" />
      <path d="M-5.5 0 H5.5 M0 -5.5 V5.5" stroke="#262626" stroke-width="1" fill="none"/>
    </symbol>
    <symbol id="icon-phone" viewBox="-7 -7 14 14">
      <path class="icon-fill" d="M-6 -2 Q0 -6 6 -2 L6 0 L3 0 L3 -1.5 L-3 -1.5 L-3 0 L-6 0 Z M-4 1 H4 L5 5 H-5 Z" />
    </symbol>
    <symbol id="icon-mail" viewBox="-7 -7 14 14">
      <rect class="icon-fill" x="-5.5" y="-4" width="11" height="8" />
      <path d="M-5.5 -4 L0 0.5 L5.5 -4" stroke="#262626" stroke-width="1" fill="none"/>
    </symbol>
    <symbol id="icon-social" viewBox="-9 -9 18 18">
      <rect class="icon-fill" x="-7.5" y="-7.5" width="15" height="15" rx="2.5" />
    </symbol>
    <symbol id="icon-pin" viewBox="-10 -12 20 24">
      <path class="icon-line" d="M0 7 C-5 1 -7 -2 -7 -4.5 A7 7 0 0 1 7 -4.5 C7 -2 5 1 0 7 Z" />
      <circle class="icon-line" cy="-4.5" r="2.5" />
      <path class="icon-line" d="M-6 6 C-9 7 -9 9.5 0 9.5 C9 9.5 9 7 6 6" />
    </symbol>
  </defs>
</svg>

<!-- Box 1: vehicle sales -->
<svg class="advert advert--sales" viewBox="0 0 737 503" role="group" aria-label="Rostane vehicle sales advert">
  <rect class="paper" width="737" height="503" />
  <rect class="band" x="0" y="24" width="520" height="121" />
  <polygon class="panel" points="382,0 737,0 737,433" />
  <polygon class="band" points="527,0 737,0 737,36 560,36" />
  <polygon class="band" points="542,171 667,171 737,258 737,418" />

  <g class="brand">
    <circle class="brand-dot" cx="62" cy="85" r="14" />
    <text class="brand-name" x="92" y="103">Rostane</text>
  </g>

  <g class="contacts on-dark">
    <text class="contact" x="674" y="79" text-anchor="end">www.Rostane.example</text>
    <text class="contact" x="674" y="103" text-anchor="end">417652</text>
    <text class="contact" x="674" y="127" text-anchor="end">sales@rostane</text>
    <use href="#icon-web" x="685" y="66" width="14" height="14" />
    <use href="#icon-phone" x="685" y="90" width="14" height="14" />
    <use href="#icon-mail" x="685" y="114" width="14" height="14" />
  </g>

  <polygon class="band" points="0,177 252,177 286,222 0,222" />
  <text class="box-title" x="28" y="210" textLength="208" lengthAdjust="spacingAndGlyphs">Vehicle SALES</text>

  <g class="features on-light">
    <use href="#icon-tick" x="28" y="250" width="16" height="16" />
    <use href="#icon-tick" x="28" y="277" width="16" height="16" />
    <use href="#icon-tick" x="28" y="304" width="16" height="16" />
    <use href="#icon-tick" x="28" y="331" width="16" height="16" />
    <text class="feature" x="56" y="265">Japanese Minivan specialist</text>
    <text class="feature" x="56" y="293">European &amp; UK vehicles supplied at best prices</text>
    <text class="feature" x="56" y="320">Vans and light commercials available</text>
    <text class="feature" x="56" y="347">Trusted supplier with <tspan class="strong">20 years experience</tspan></text>
  </g>

  <polygon class="band" points="0,385 392,385 422,419 0,419" />
  <use class="on-dark" href="#icon-social" x="28" y="393" width="18" height="18" />
  <text class="bar-text" x="60" y="409">social.example/rostanemotortrading</text>

  <polygon class="band" points="0,438 667,438 697,476 0,476" />
  <use class="on-dark" href="#icon-pin" x="28" y="445" width="20" height="24" />
  <text class="bar-text" x="62" y="464">Petites Vergees Lane, Les Corvets, GY9 7QX</text>
</svg>

<!-- Box 2: service and repairs -->
<svg class="advert advert--service" viewBox="0 0 737 503" role="group" aria-label="Rostane service and repairs advert">
  <rect class="paper" width="737" height="503" />
  <rect class="band" x="217" y="24" width="520" height="121" />
  <polygon class="panel" points="0,0 355,0 0,433" />
  <polygon class="band" points="0,0 210,0 177,36 0,36" />
  <polygon class="band" points="195,171 70,171 0,258 0,418" />

  <g class="brand">
    <circle class="brand-dot" cx="381" cy="85" r="14" />
    <text class="brand-name" x="411" y="103">Rostane</text>
  </g>

  <g class="contacts on-dark">
    <use href="#icon-web" x="38" y="66" width="14" height="14" />
    <use href="#icon-phone" x="38" y="90" width="14" height="14" />
    <use href="#icon-mail" x="38" y="114" width="14" height="14" />
    <text class="contact" x="63" y="79">www.Rostane.example</text>
    <text class="contact" x="63" y="103">417652</text>
    <text class="contact" x="63" y="127">sales@rostane</text>
  </g>

  <polygon class="band" points="217,178 737,178 737,222 185,222" />
  <text class="box-title" x="235" y="211" textLength="474" lengthAdjust="spacingAndGlyphs">Service and repairs to all models</text>

  <g class="features on-light">
    <text class="feature" x="680" y="266" text-anchor="end">Popular <tspan class="strong">£99</tspan> service health check</text>
    <text class="feature" x="680" y="293" text-anchor="end">Qualified mechanics</text>
    <text class="feature" x="680" y="320" text-anchor="end">Wheel alignment &amp; Air conditioning</text>
    <text class="feature" x="680" y="347" text-anchor="end">Fleet servicing options</text>
    <use href="#icon-tick" x="692" y="251" width="16" height="16" />
    <use href="#icon-tick" x="692" y="278" width="16" height="16" />
    <use href="#icon-tick" x="692" y="305" width="16" height="16" />
    <use href="#icon-tick" x="692" y="332" width="16" height="16" />
  </g>

  <polygon class="band" points="345,385 737,385 737,419 315,419" />
  <text class="bar-text" x="676" y="409" text-anchor="end">social.example/rostanemotortrading</text>
  <use class="on-dark" href="#icon-social" x="691" y="393" width="18" height="18" />

  <polygon class="band" points="70,438 737,438 737,476 40,476" />
  <text class="bar-text" x="674" y="464" text-anchor="end">Petites Vergees Lane, Les Corvets, GY9 7QX</text>
  <use class="on-dark" href="#icon-pin" x="688" y="445" width="20" height="24" />
</svg>

</body>
</html>
```